TIPSY PANTRY needs a show poster

"Tipsy Pantry" is a stand up comedy show. We need a fun, eye-catching poster. The taglines are "Loads of Laughter" and "Clean Comedy, Dirty Martinis." We are attaching our logo files and a vintage photo that we sometimes use, but they do not need to be a part of the poster. We like vintage* and retro* images but are open to the creativity of the designer.

* Added note: Vintage and Retro to us means 1950s-1970s design types, not distressed and worn looking. Color is good!

Target Market(s)

Women & Couples, Ages 30-70

Industry/Entity Type

Comedy

Requirements
Must have
• Title: Tipsy Pantry
• Primary Tagline: Loads of Laughs
• Performers Names: Helen Forsyth & Joan Pettibrook
Nice to have
• Secondary Tagline: Clean Comedy, Dirty Martinis.
Should not have
• No cliche images of stand up comedy (spotlight, stage, microphone)

```html
<!DOCTYPE html>
<html lang="en">
<head>
<meta charset="utf-8">
<title>Loads of Laughter — Tipsy Pantry</title>
<link rel="stylesheet" href="https://fonts.googleapis.com/css2?family=Sniglet:wght@400;800&family=Titan+One&display=swap">
<style>
  :root {
    --teal: #37a59c;
    --teal-dark: #2a9389;
    --cream: #fcf6d8;
    --orange: #d46133;
    --ink: #111111;
    --sage: #a3c9ac;
    --bottle: #5a9a80;
  }
  * { margin: 0; padding: 0; box-sizing: border-box; }
  html, body { width: 862px; height: 1200px; overflow: hidden; background: var(--teal); }
  .poster {
    position: relative;
    width: 862px;
    height: 1200px;
    background: var(--teal);
    overflow: hidden;
    font-family: "Sniglet", sans-serif;
  }
  .title {
    position: absolute;
    top: 52px;
    left: 0;
    width: 100%;
    text-align: center;
    font-family: "Sniglet", sans-serif;
    font-weight: 800;
    font-size: 112px;
    line-height: 124px;
    color: var(--cream);
    letter-spacing: 2px;
    text-shadow:
      -3px -3px 0 var(--orange), 3px -3px 0 var(--orange),
      -3px 3px 0 var(--orange), 3px 3px 0 var(--orange),
      0 -4px 0 var(--orange), 0 4px 0 var(--orange),
      -4px 0 0 var(--orange), 4px 0 0 var(--orange),
      7px 8px 0 var(--ink);
  }
  .artwork {
    position: absolute;
    left: 0;
    top: 0;
    width: 862px;
    height: 1200px;
  }
  .performer-disc {
    position: absolute;
    width: 178px;
    height: 178px;
    border-radius: 50%;
    background: var(--teal-dark);
    display: flex;
    align-items: center;
    justify-content: center;
    text-align: center;
    font-size: 34px;
    line-height: 36px;
    color: var(--ink);
  }
  .performer-disc.left { left: 106px; top: 813px; }
  .performer-disc.right { left: 580px; top: 807px; }
  .event-detail {
    position: absolute;
    top: 1043px;
    font-family: "Titan One", sans-serif;
    font-size: 20px;
    line-height: 29px;
    color: var(--orange);
    text-transform: uppercase;
    text-shadow: 2px 2px 0 var(--ink);
  }
  .event-detail.date { left: 64px; }
  .event-detail.venue { left: 648px; }
  .host-name {
    position: absolute;
    left: 0;
    width: 100%;
    top: 1012px;
    text-align: center;
    font-family: "Titan One", sans-serif;
    font-size: 50px;
    line-height: 54px;
    color: var(--cream);
  }
</style>
</head>
<body>
<main class="poster">
  <h1 class="title">Loads of<br>Laughter</h1>

  <svg class="artwork" viewBox="0 0 862 1200" xmlns="http://www.w3.org/2000/svg">
    <defs>
      <linearGradient id="scene-tones" x1="0" y1="0" x2="1" y2="1">
        <stop offset="0" stop-color="#d46133"/>
        <stop offset="0.45" stop-color="#e9dcb8"/>
        <stop offset="0.75" stop-color="#6fa88e"/>
        <stop offset="1" stop-color="#d46133"/>
      </linearGradient>
      <path id="arc-standup" d="M420 428 Q470 360 556 352"/>
      <path id="arc-clean" d="M38 682 Q180 580 368 648"/>
      <path id="arc-dirty" d="M478 712 Q620 760 830 622"/>
    </defs>
    <rect class="illustration" x="173" y="350" width="506" height="445" rx="40"
          fill="url(#scene-tones)" opacity="0.9"
          role="img" aria-label="Retro illustration of three stylish women in sunglasses toasting with martinis beside a wine bottle"/>
    <g font-family="Sniglet, sans-serif" fill="#111111">
      <text font-size="28"><textPath href="#arc-standup">Stand-up</textPath></text>
      <text font-size="40"><textPath href="#arc-clean">Clean Comedy</textPath></text>
      <text font-size="40"><textPath href="#arc-dirty">Dirty Martinis</textPath></text>
    </g>
  </svg>

  <div class="performer-disc left">Joan<br>Pettibrook</div>
  <div class="performer-disc right">Helen<br>Forsyth</div>

  <p class="event-detail date">Thursday,<br>November<br>28</p>
  <p class="host-name">TIPSY<br>PANTRY</p>
  <p class="event-detail venue">Cafe Hall<br>Door open<br>7 PM</p>
</main>
</body>
</html>
```